Jewelry & Bead Show company needs a compelling flyer design

We're a jewelry & bead show organizer, producing over 40 shows a year in different U.S. cities. We need a flyer design that excites customers (who are mainly women), and makes them want to attend the shows. Our show exhibitors are gem/jewelry/bead dealers from around the world, selling merchandise ranging from $1 to thousands of dollars a piece. Flyer dimensions are 6.5" H x 8.5" W, double-sided. The mailing label must be 3" H x 4.5" W. Flyer template is attached.

Target Market(s)

Women 18+

Industry/Entity Type

It Company

Requirements
Must have
• Here are messages to be included:
• -Lustra Fest (big & bold)
• -Why wait, buy on site with confidence at Lustra Fest! Connect face to face with the direct source and Artisans for latest fashion & the best deals!
• -Your FREE pass enclosed
• -Show city, date & facility
• On the back side, there must be an area for show calendar (dates & cities), enough space for 10 shows
Nice to have
• An image of crowd/attendees shopping at a jewelry show.
Should not have
• Diamond images

```html
<!DOCTYPE html>
<html lang="en">
<head>
<meta charset="UTF-8">
<title>Lustra Fest – Show Flyer</title>
<link href="https://fonts.googleapis.com/css2?family=Oswald:wght@400;500;600&family=Lato:wght@400;700;900&display=swap" rel="stylesheet">
<style>
  :root{
    --page:#ece9e6;
    --paper:#ffffff;
    --brand-red:#c2472f;
    --deep-red:#8e2a1a;
    --row-red:#c65a42;
    --ink:#3a3533;
    --muted:#8a8480;
    --button:#3d3937;
    --button-text:#f2c9a8;
    --photo-warm-a:#d9c7b5;
    --photo-warm-b:#9c7e66;
    --photo-dark-a:#3b2d2a;
    --photo-dark-b:#b79a8a;
    --panel-grey:#cfcfcf;
    --rule:#c9c4c0;
  }
  *{box-sizing:border-box;margin:0;padding:0}
  html,body{width:900px;height:1200px;overflow:hidden;background:var(--page)}
  body{position:relative;font-family:"Lato",Arial,sans-serif;color:var(--ink)}
  .flyer{position:absolute;left:78px;width:744px;height:569px;background:var(--paper);overflow:hidden;box-shadow:0 2px 8px rgba(0,0,0,.18)}
  .flyer--front{top:20px}
  .flyer--back{top:611px}
  .flyer__shapes{position:absolute;inset:0}
  .brand{position:absolute;display:flex;align-items:center;gap:10px}
  .brand__mark{width:14px;height:14px;border-radius:50%;background:var(--brand-red)}
  .brand__name{font-family:"Lato",Arial,sans-serif;font-weight:900;color:var(--brand-red);font-size:40px;letter-spacing:1px;text-transform:uppercase;line-height:1}
  .flyer--front .brand{left:28px;top:50px}
  .flyer--back .brand{left:470px;top:490px}
  .flyer--back .brand__name{font-size:34px}

  .pitch{position:absolute;left:0;top:235px;width:410px;text-align:center;color:#fff}
  .pitch__title{font-family:"Oswald",Arial,sans-serif;font-weight:500;font-size:40px;letter-spacing:2px;line-height:1}
  .pitch__sub{font-family:"Oswald",Arial,sans-serif;font-size:12px;letter-spacing:1.2px;margin-top:6px;text-transform:uppercase}
  .pitch__rule{width:290px;height:1px;background:rgba(255,255,255,.8);margin:14px auto}
  .pitch__body{font-family:"Oswald",Arial,sans-serif;font-size:14px;letter-spacing:.8px;line-height:1.45;text-transform:uppercase;width:300px;margin:0 auto}
  .pitch__pass{display:inline-block;margin-top:22px;background:var(--button);color:var(--button-text);font-family:"Oswald",Arial,sans-serif;font-size:19px;letter-spacing:1.5px;padding:9px 26px;border-radius:22px;text-transform:uppercase}

  .mailing{position:absolute;left:440px;top:238px;width:280px}
  .mailing__sender{font-size:10px;color:var(--ink)}
  .mailing__stamp{position:absolute;right:0;top:-6px;width:82px;height:40px;border:1px solid var(--ink);font-size:7px;line-height:1.25;text-align:center;padding:6px 4px}
  .mailing__return{margin-top:48px;font-weight:700;color:var(--brand-red);font-size:13px;letter-spacing:.5px}
  .mailing__lines{margin-top:34px;list-style:none}
  .mailing__lines li{height:1px;background:var(--ink);margin-bottom:26px}

  .schedule{position:absolute;left:362px;top:18px;width:362px}
  .schedule__head,.schedule__row{display:grid;grid-template-columns:1fr 110px}
  .schedule__head{font-family:"Oswald",Arial,sans-serif;font-weight:500;font-size:20px;color:var(--ink);padding:4px 14px 8px;border-bottom:2px solid var(--brand-red)}
  .schedule__head span:last-child{text-align:center}
  .schedule__rows{list-style:none;margin-top:6px}
  .schedule__row{background:var(--row-red);color:#fff;font-size:11px;height:30px;align-items:center;padding:0 14px;margin-bottom:4px}
  .schedule__row span:last-child{text-align:center;border-left:1px solid rgba(255,255,255,.5)}
</style>
</head>
<body>

<section class="flyer flyer--front">
  <svg class="flyer__shapes" width="744" height="569" viewBox="0 0 744 569">
    <defs>
      <linearGradient id="shopperPhoto" x1="0" y1="0" x2="1" y2="1">
        <stop offset="0" stop-color="var(--photo-warm-a)"/>
        <stop offset="1" stop-color="var(--photo-warm-b)"/>
      </linearGradient>
    </defs>
    <path role="img" aria-label="Photo of shoppers examining jewelry at a show counter" d="M300,0 L744,0 L744,170 Q560,200 420,150 Q340,120 300,60 Z" fill="url(#shopperPhoto)"/>
    <path d="M0,200 Q220,150 430,215 Q600,260 744,175" fill="none" stroke="var(--deep-red)" stroke-width="3"/>
    <path d="M0,212 Q220,168 410,225 L410,556 L0,556 Z" fill="var(--brand-red)"/>
    <rect x="0" y="556" width="410" height="5" fill="var(--deep-red)"/>
  </svg>

  <div class="brand"><span class="brand__name">Lustra Fest</span><span class="brand__mark"></span></div>

  <div class="pitch">
    <h1 class="pitch__title">WHY WAIT</h1>
    <p class="pitch__sub">Buy on site with confidence at Lustra Fest!</p>
    <div class="pitch__rule"></div>
    <p class="pitch__body">Connect face to face with the direct source and Artisans for latest fashion &amp; the best deals!</p>
    <div class="pitch__rule"></div>
    <span class="pitch__pass">Your free pass enclosed</span>
  </div>

  <div class="mailing">
    <p class="mailing__sender">Company / Mailing Address</p>
    <div class="mailing__stamp">Presorted Standard U.S. Postage Paid</div>
    <p class="mailing__return">RETURN SERVICE REQUESTED</p>
    <ul class="mailing__lines"><li></li><li></li><li></li><li></li></ul>
  </div>
</section>

<section class="flyer flyer--back">
  <svg class="flyer__shapes" width="744" height="569" viewBox="0 0 744 569">
    <defs>
      <linearGradient id="modelPhoto" x1="0" y1="0" x2="1" y2="1">
        <stop offset="0" stop-color="var(--photo-dark-a)"/>
        <stop offset="1" stop-color="var(--photo-dark-b)"/>
      </linearGradient>
    </defs>
    <rect x="0" y="300" width="330" height="269" fill="var(--panel-grey)"/>
    <path role="img" aria-label="Photo of a woman wearing jewelry beside scattered colorful gemstones" d="M0,0 L330,0 L330,240 Q260,320 140,320 L0,320 Z" fill="url(#modelPhoto)"/>
    <path d="M330,0 L330,240 Q260,320 140,320 L0,320" fill="none" stroke="var(--brand-red)" stroke-width="4"/>
    <path d="M390,480 Q560,430 744,470" fill="none" stroke="var(--brand-red)" stroke-width="3"/>
    <path d="M390,548 Q560,580 744,540" fill="none" stroke="var(--deep-red)" stroke-width="3"/>
  </svg>

  <div class="schedule">
    <div class="schedule__head"><span>SHOW CITY</span><span>DATE</span></div>
    <ul class="schedule__rows">
      <li class="schedule__row"><span>Lorem Ipsum</span><span>00-00-00</span></li>
      <li class="schedule__row"><span>Lorem Ipsum</span><span>00-00-00</span></li>
      <li class="schedule__row"><span>Lorem Ipsum</span><span>00-00-00</span></li>
      <li class="schedule__row"><span>Lorem Ipsum</span><span>00-00-00</span></li>
      <li class="schedule__row"><span>Lorem Ipsum</span><span>00-00-00</span></li>
      <li class="schedule__row"><span>Lorem Ipsum</span><span>00-00-00</span></li>
      <li class="schedule__row"><span>Lorem Ipsum</span><span>00-00-00</span></li>
      <li class="schedule__row"><span>Lorem Ipsum</span><span>00-00-00</span></li>
      <li class="schedule__row"><span>Lorem Ipsum</span><span>00-00-00</span></li>
      <li class="schedule__row"><span>Lorem Ipsum</span><span>00-00-00</span></li>
    </ul>
  </div>

  <div class="brand"><span class="brand__name">Lustra Fest</span><span class="brand__mark"></span></div>
</section>

</body>
</html>
```